New Year's Greeting from Halvorsen Financial

A EDDM Post Card to a 55+ Retirement community. 6x9 inch postcard. Happy New Year greeting with a call for a free "Financial Check-up" to start the New Year. Include company logo and contact information.
see sampple files.

Industry/Entity Type

Financial

Requirements
Must have
• After Christmas so New Year only Greeting

```html
<!DOCTYPE html>
<html lang="en">
<head>
<meta charset="utf-8">
<title>Halvorsen Financial – New Year Postcard</title>
<link rel="stylesheet" href="https://fonts.googleapis.com/css2?family=Open+Sans:wght@400;600&family=Roboto+Condensed:wght@400;700&display=swap">
<style>
  :root {
    --navy: #2e3387;
    --navy-light: #4a52b0;
    --navy-deep: #232870;
    --grey-text: #555a60;
    --red: #e0242b;
    --white: #ffffff;
    --page: #c4c4c4;
    --photo-warm: #d8c9b8;
    --photo-cool: #e9eef5;
    --gold: #d9aa3e;
    --gold-soft: #f3e2b3;
  }
  * { margin: 0; padding: 0; box-sizing: border-box; }
  html, body { width: 1003px; height: 1200px; overflow: hidden; }
  body { background: var(--page); position: relative; font-family: "Open Sans", sans-serif; }
  .card { position: absolute; left: 122px; width: 760px; height: 507px; background: var(--white); overflow: hidden; }
  .card--front { top: 54px; }
  .card--back { top: 630px; }
  .abs { position: absolute; }
  .swoosh { position: absolute; left: 0; top: 0; width: 760px; height: 507px; }
  .cond { font-family: "Roboto Condensed", sans-serif; font-weight: 700; }

  /* front */
  .brand { left: 0; top: 0; width: 606px; height: 108px; display: flex; align-items: center; justify-content: center; gap: 12px; }
  .brand__mark { width: 40px; height: 40px; background: var(--navy); }
  .brand__name { color: var(--navy); font-size: 30px; font-weight: 400; letter-spacing: 2px; line-height: 1.05; text-transform: uppercase; }
  .topic-band { left: 0; top: 108px; width: 606px; height: 68px; background: var(--navy); color: var(--white); text-align: center; }
  .topic-band__title { font-size: 42px; line-height: 1; padding-top: 4px; letter-spacing: -0.5px; }
  .topic-band__sub { font-size: 15px; }
  .portrait-front { left: 606px; top: 0; width: 154px; height: 218px; background: linear-gradient(160deg, var(--navy-light), var(--navy-deep)); }
  .advisor-front { left: 409px; top: 186px; width: 170px; text-align: right; color: var(--navy); }
  .advisor__name { font-size: 22px; line-height: 1; }
  .advisor__title { font-size: 8px; font-weight: 600; letter-spacing: .4px; text-transform: uppercase; }
  .bells { left: 20px; top: 194px; width: 162px; height: 100px; border-radius: 8px;
    background: linear-gradient(180deg, var(--gold-soft), var(--gold)); opacity: .85; }
  .free-badge { left: 31px; top: 272px; width: 148px; height: 148px; border-radius: 50%;
    background: var(--red); color: var(--white); display: flex; align-items: center; justify-content: center; font-size: 52px; }
  .greeting { right: 56px; top: 258px; text-align: right; color: var(--white); }
  .greeting__lead { font-size: 25px; line-height: 1.2; }
  .greeting__headline { font-size: 56px; line-height: 1.05; letter-spacing: .3px; }
  .greeting__tail { font-size: 24px; line-height: 1.15; }
  .contact-front { left: 220px; top: 412px; color: var(--grey-text); text-align: center; }
  .contact__phone { display: flex; align-items: center; justify-content: center; gap: 10px; font-size: 41px; line-height: 1.1; }
  .contact__web { font-size: 29px; line-height: 1.1; }

  /* back */
  .back-header { left: 0; top: 0; width: 578px; height: 78px; background: var(--navy); color: var(--white); text-align: center; padding-top: 8px; }
  .back-header__title { font-size: 35px; line-height: 1; }
  .back-header__sub { font-size: 20px; line-height: 1.2; margin-top: 3px; }
  .stamp { left: 622px; top: 14px; width: 100px; height: 88px; border: 1px solid #9c9c9c; }
  .services-pill { left: 297px; top: 96px; width: 149px; height: 28px; border-radius: 10px; background: var(--navy); color: var(--white); font-size: 23px; text-align: center; line-height: 28px; }
  .services-intro { left: 138px; top: 128px; width: 600px; font-size: 16.5px; line-height: 1.12; color: #333; }
  .photo-clients { left: 0; top: 170px; width: 390px; height: 196px;
    background: radial-gradient(ellipse at 55% 55%, var(--photo-warm), var(--photo-cool) 70%, var(--white)); }
  .services-list { left: 404px; top: 164px; list-style: none; color: #333; font-size: 17.5px; }
  .services-list li { display: flex; align-items: center; height: 24px; gap: 18px; }
  .tick { width: 18px; height: 18px; }
  .portrait-back { left: 594px; top: 166px; width: 176px; height: 176px; border-radius: 50%; border: 6px solid var(--navy);
    background: linear-gradient(160deg, #f2f2f2, #c9cbd6); }
  .advisor-back { left: 578px; top: 334px; width: 182px; height: 46px; background: var(--navy); color: var(--white); text-align: center; padding-top: 6px; }
  .contact-back { left: 80px; top: 398px; color: var(--white); text-align: center; }
  .contact-back .contact__phone { font-size: 50px; }
  .contact-back .contact__web { font-size: 34px; }
  .mail-box { left: 549px; top: 387px; width: 192px; height: 114px; background: var(--white); font-family: Arial, sans-serif; font-size: 11px; color: #222; padding: 38px 14px 0; }
  .mail-box__code { text-align: center; margin-bottom: 16px; }
  .mail-box__addr { line-height: 1.2; }
</style>
</head>
<body>

<section class="card card--front" aria-label="Postcard front">
  <svg class="swoosh" viewBox="0 0 760 507" aria-hidden="true">
    <defs>
      <linearGradient id="frontBand" x1="0" x2="1" y1="0" y2="0">
        <stop offset="0" stop-color="#6a70c6"/>
        <stop offset=".35" stop-color="#3a40a0"/>
        <stop offset="1" stop-color="#2e3387"/>
      </linearGradient>
    </defs>
    <path d="M0,206 C200,240 450,250 760,186 L760,434 C450,370 200,400 0,458 Z" fill="url(#frontBand)"/>
    <path d="M140,228 C320,254 520,240 760,178" fill="none" stroke="#a3a5ad" stroke-width="5"/>
    <path d="M0,466 C200,408 450,378 760,442" fill="none" stroke="#a3a5ad" stroke-width="6"/>
  </svg>

  <div class="abs brand">
    <span class="brand__mark" aria-hidden="true"></span>
    <span class="brand__name">Halvorsen<br>Financial</span>
  </div>

  <div class="abs topic-band">
    <div class="topic-band__title cond">Investing &amp; Retirement</div>
    <div class="topic-band__sub">A Focus on Growth and Income</div>
  </div>

  <div class="abs portrait-front" role="img" aria-label="Portrait photo of the financial planner"></div>

  <div class="abs advisor-front">
    <div class="advisor__name cond">PAUL WHITAKER</div>
    <div class="advisor__title">Certified Financial Planner™</div>
  </div>

  <div class="abs bells" role="img" aria-label="Illustration of golden holiday bells with a red bow"></div>
  <div class="abs free-badge cond">FREE</div>

  <div class="abs greeting">
    <div class="greeting__lead">Happy New Year greeting with a call for a</div>
    <div class="greeting__headline cond">Financial Check-up</div>
    <div class="greeting__tail">to start the New Year</div>
  </div>

  <div class="abs contact-front">
    <div class="contact__phone cond">
      <svg width="34" height="34" viewBox="0 0 34 34" aria-hidden="true">
        <circle cx="17" cy="17" r="15" fill="none" stroke="#2e3387" stroke-width="2.5"/>
        <path d="M11,9 l4,0 l1,5 l-2,2 c1,3 3,5 6,6 l2,-2 l5,1 l0,4 c-10,1 -17,-6 -16,-16z" fill="#2e3387"/>
      </svg>
      <span>(555) 214-0186</span>
    </div>
    <div class="contact__web cond">www.halvorsenfinancial.com</div>
  </div>
</section>

<section class="card card--back" aria-label="Postcard back">
  <svg class="swoosh" viewBox="0 0 760 507" aria-hidden="true">
    <defs>
      <linearGradient id="backBand" x1="0" x2="1" y1="0" y2="0">
        <stop offset="0" stop-color="#2e3387"/>
        <stop offset=".6" stop-color="#4a52b0"/>
        <stop offset="1" stop-color="#2e3387"/>
      </linearGradient>
    </defs>
    <path d="M0,346 C250,392 500,384 760,352 L760,507 L0,507 Z" fill="url(#backBand)"/>
    <path d="M0,338 C250,384 500,376 760,344" fill="none" stroke="#a3a5ad" stroke-width="5"/>
  </svg>

  <div class="abs back-header">
    <div class="back-header__title cond">Free Financial Check-up</div>
    <div class="back-header__sub cond">After Christmas so New Year only Greeting</div>
  </div>

  <div class="abs stamp" aria-label="Postage area"></div>

  <div class="abs photo-clients" role="img" aria-label="Photo of an advisor shaking hands with a senior couple"></div>

  <div class="abs services-pill cond">Our Services:</div>
  <p class="abs services-intro">Our goal is to provide you with unparalleled service in the following areas of expertise that includes:</p>

  <ul class="abs services-list">
    <li><svg class="tick" viewBox="0 0 18 18" aria-hidden="true"><rect x="1" y="4" width="13" height="13" fill="#2e3387"/><path d="M4,10 l4,4 l9,-13" fill="none" stroke="#2aa8e0" stroke-width="3"/></svg>Financial Planning</li>
    <li><svg class="tick" viewBox="0 0 18 18" aria-hidden="true"><rect x="1" y="4" width="13" height="13" fill="#2e3387"/><path d="M4,10 l4,4 l9,-13" fill="none" stroke="#2aa8e0" stroke-width="3"/></svg>Employee Benefits</li>
    <li><svg class="tick" viewBox="0 0 18 18" aria-hidden="true"><rect x="1" y="4" width="13" height="13" fill="#2e3387"/><path d="M4,10 l4,4 l9,-13" fill="none" stroke="#2aa8e0" stroke-width="3"/></svg>Insurance</li>
    <li><svg class="tick" viewBox="0 0 18 18" aria-hidden="true"><rect x="1" y="4" width="13" height="13" fill="#2e3387"/><path d="M4,10 l4,4 l9,-13" fill="none" stroke="#2aa8e0" stroke-width="3"/></svg>College Funding</li>
    <li><svg class="tick" viewBox="0 0 18 18" aria-hidden="true"><rect x="1" y="4" width="13" height="13" fill="#2e3387"/><path d="M4,10 l4,4 l9,-13" fill="none" stroke="#2aa8e0" stroke-width="3"/></svg>Retirement Plans</li>
    <li><svg class="tick" viewBox="0 0 18 18" aria-hidden="true"><rect x="1" y="4" width="13" height="13" fill="#2e3387"/><path d="M4,10 l4,4 l9,-13" fill="none" stroke="#2aa8e0" stroke-width="3"/></svg>Estate Planning</li>
    <li><svg class="tick" viewBox="0 0 18 18" aria-hidden="true"><rect x="1" y="4" width="13" height="13" fill="#2e3387"/><path d="M4,10 l4,4 l9,-13" fill="none" stroke="#2aa8e0" stroke-width="3"/></svg>Charitable Giving</li>
  </ul>

  <div class="abs portrait-back" role="img" aria-label="Circular portrait photo of the financial planner"></div>

  <div class="abs advisor-back">
    <div class="advisor__name cond">PAUL WHITAKER</div>
    <div class="advisor__title">Certified Financial Planner™</div>
  </div>

  <div class="abs contact-back">
    <div class="contact__phone cond">
      <svg width="42" height="42" viewBox="0 0 34 34" aria-hidden="true">
        <circle cx="17" cy="17" r="15" fill="none" stroke="#ffffff" stroke-width="2.5"/>
        <path d="M11,9 l4,0 l1,5 l-2,2 c1,3 3,5 6,6 l2,-2 l5,1 l0,4 c-10,1 -17,-6 -16,-16z" fill="#ffffff"/>
      </svg>
      <span>(555) 214-0186</span>
    </div>
    <div class="contact__web cond">www.halvorsenfinancial.com</div>
  </div>

  <div class="abs mail-box">
    <div class="mail-box__code">*********ECRWSS*********</div>
    <div class="mail-box__addr">Local<br>Postal Customer</div>
  </div>
</section>

</body>
</html>
```